Luxury Tours Design

We are “Velvet Harbour” a Chauffeur Company based in Maidenhead, Berkshire. Our website is - velvetharbour-example.co.uk which will give you an insite into the Company.
Our clients consist of luxurious Hotels, large Corporate Companies along with private UHNW clients.
We have a fleet of Calvani E, S and V Class vehicles along with 16 Seater Executive Coaches so we can accommodate single travellers, couples, friends, families and groups.
We would like an A5 (or slightly larger) double sided colour leaflet designed to promote our Tours in our local and surrounding areas.
The information below is some indication as to what we would like.
On the front we would like:-
Velvet Harbour “Heritage Loop” This will be our main promoting Tour
Slogan “Velvet Harbour….every mile, with care”
Tour will include:-
Visiting the historic town of Windsor, Ashdene Keep, St Aldric’s Chantry and Grand Fennick Trading Gallery.
Then onto Eton (Hollins Academy) and a lovely view of the River Thames along with an array of Antique Shops in the quaint streets.
Bray Village (Heron Holm), renowed for it’s Gourmandine Star Restaurants and pubs.
Through picturesque Cookham along to Marlow for some shopping in the boutique shops, small listed buildings and beautiful places for refreshments, along with stunning views of the River Thames form Pellow Crossing.
This will be our main tour we offer but again this is flexible. This aims to be around 4-5 hours.
On the front, a picture of Ashdene keep maybe a large picture with writing over the top, or a separate photo….. a couple of photos attached or something similar.
On the back of the leaflet:-
We offer London based tours including:-
Bexleys, Fernmoor Green, Redcliffe Manor House, Ormsby Crown House, Quillerton Plaza, Parade of the Lancers, Keep of Aldermoor, Old Tom, Calderbrook Minster to name a few! Or maybe London by night with a show or restaurant.
On the back a picture of Ormsby Crown House…a couple of picture are also attached or again something similar.
Other Tours provided:-
Farrowdale Hall Palace, Oxford and Durnford Palace, Greyrock Ring and Bath, The Cotswolds, Stratford and Pendry Castle, Lorrimer Outlet Village.
Also bespoke Tours can be arranged. We can personalise any tour to your requirements.
Experienced friendly Chauffeur’s, no request too big or small.
Please call us on 01632 960472 or email us sales@velvetharbour-example.co.uk
Please can you do an initial design including the above information.
Look forward to hearing from you.
Kind regards
Please visit https://www.brookmereprivatedrivers-example.co.uk/ to get an idea of the tours of London to go on the back.
Prices will follow to be added after design and layout has been done.
Our VH logo is available on www.velvetharbour-example.co.uk
We want text to be editable and also for the design to have a luxury feel.
Chauffeur

```html
<!DOCTYPE html>
<html lang="en">
<head>
<meta charset="utf-8">
<title>Velvet Harbour – Heritage Loop Leaflet</title>
<link href="https://fonts.googleapis.com/css2?family=Montserrat:wght@400;500;600;700;800&family=Oswald:wght@700&display=swap" rel="stylesheet">
<style>
  :root{
    --backdrop:#5b5b5b;
    --ink:#1e1e1e;
    --stone-dark:#45423b;
    --band:#45433c;
    --paper:#ffffff;
    --contact:#070707;
    --contact-text:#f4f4f4;
    --rule:#45423b;
  }
  *{box-sizing:border-box;margin:0;padding:0}
  html,body{width:1200px;height:775px;overflow:hidden}
  body{background:var(--backdrop);font-family:"Montserrat",sans-serif;color:var(--ink);position:relative}

  .leaflet{position:absolute;top:37px;width:500px;height:700px;background:var(--paper);overflow:hidden;box-shadow:0 6px 18px rgba(0,0,0,.35)}
  .leaflet--front{left:80px}
  .leaflet--back{left:620px}

  /* FRONT */
  .hero-photo{position:absolute;left:0;top:0;width:500px;height:310px;
    background:linear-gradient(180deg,#e6ebf2 0%,#c9d2dc 30%,#b9b2a0 45%,#7f8f5c 60%,#4f7a2c 80%,#3d6422 100%)}
  .brand{position:absolute;top:26px;left:0;width:100%;display:flex;justify-content:center;align-items:center;gap:9px}
  .brand__mark{width:22px;height:22px;border-radius:50%;background:var(--stone-dark)}
  .brand__name{font-size:21px;font-weight:500;color:var(--stone-dark);letter-spacing:.3px}
  .tour-title{position:absolute;top:58px;left:0;width:100%;text-align:center;font-family:"Oswald",sans-serif;font-weight:700;font-size:50px;line-height:1;color:var(--stone-dark);letter-spacing:.5px}
  .tour-sub{position:absolute;top:116px;left:0;width:100%;text-align:center;font-size:14px;font-weight:700;color:var(--ink)}

  .slogan-band{position:absolute;left:0;top:302px;width:500px;height:44px;background:var(--band);display:flex;align-items:center;justify-content:center}
  .slogan-band span{color:#fff;font-weight:700;font-size:17px;letter-spacing:.6px;text-transform:uppercase}

  .itinerary{position:absolute;left:24px;top:358px;width:452px}
  .itinerary__heading{font-size:12.5px;font-weight:800;color:var(--stone-dark);padding-bottom:3px;border-bottom:1.5px solid var(--rule);margin-bottom:7px;text-transform:uppercase}
  .itinerary__list{list-style:none;border-left:1.5px dotted #777;margin-left:6px;padding-left:0}
  .itinerary__item{position:relative;padding-left:16px;font-size:10.8px;line-height:1.36;margin-bottom:5px;color:#222}
  .itinerary__item:last-child{margin-bottom:0}
  .itinerary__item--narrow{max-width:230px}
  .itinerary__item svg{position:absolute;left:-7px;top:2px;width:12px;height:12px;background:#fff}

  .castle-photo{position:absolute;right:0;top:548px;width:250px;height:152px;
    clip-path:polygon(14% 0,100% 0,100% 100%,0 100%);
    background:linear-gradient(180deg,#aab4bf 0%,#b5aa92 30%,#5f8a3a 55%,#3f6a25 100%)}

  .contact{position:absolute;left:0;bottom:0;height:140px;background:var(--contact);color:var(--contact-text);padding:14px 0 0 26px}
  .leaflet--front .contact{width:500px}
  .contact__heading{font-size:13px;font-weight:800;margin-bottom:6px;text-transform:uppercase}
  .contact__row{display:flex;align-items:flex-start;gap:8px;font-size:11.5px;line-height:1.3;margin-bottom:4px}
  .contact__icon{flex:none;width:16px;height:16px;margin-top:1px}

  /* BACK */
  .guards-photo{position:absolute;left:0;top:0;width:500px;height:210px;
    background:linear-gradient(180deg,#cfe0f3 0%,#dfe9f5 25%,#c8bfa8 40%,#b3aa95 62%,#b34b3a 78%,#c9a789 88%,#b99a7c 100%)}
  .palace-photo{position:absolute;left:0;top:210px;width:500px;height:340px;
    background:linear-gradient(180deg,#ffffff 0%,#e8eff7 25%,#c8d8ea 45%,#d8d3c6 60%,#bfb8a6 72%,#d8c12e 84%,#c8281e 100%)}
  .tour-copy{position:absolute;left:22px;top:222px;width:456px;font-size:10.6px;font-weight:600;line-height:1.4;color:#1f1f1f}
  .tour-copy__heading{font-weight:800;font-size:11px;color:var(--stone-dark);text-transform:uppercase}
  .tour-copy p{margin-bottom:5px;text-align:justify}
  .location-map{position:absolute;right:0;top:475px;width:265px;height:225px;
    background:linear-gradient(135deg,#eef1f2 0%,#e3ecdf 45%,#eef1f2 70%,#d6e8d3 100%)}
  .leaflet--back .contact{width:235px;height:155px;padding-left:20px}
  .leaflet--back .contact__row{font-size:10px;gap:7px}
</style>
</head>
<body>

<section class="leaflet leaflet--front">
  <div class="hero-photo" role="img" aria-label="Photo of Ashdene Keep at the end of a long tree-lined avenue under a pale sky"></div>
  <div class="brand"><span class="brand__mark"></span><span class="brand__name">Velvet Harbour</span></div>
  <h1 class="tour-title">HERITAGE LOOP</h1>
  <p class="tour-sub">This will be our main promoting Tour</p>

  <div class="slogan-band"><span>Velvet Harbour......every mile, with care</span></div>

  <div class="itinerary">
    <h2 class="itinerary__heading">Tour will include :</h2>
    <ul class="itinerary__list">
      <li class="itinerary__item"><svg viewBox="0 0 12 12"><circle cx="6" cy="6" r="5" fill="none" stroke="#333" stroke-width="1.2"/><path d="M3.5 6.2l1.8 1.8 3.4-3.6" fill="none" stroke="#333" stroke-width="1.3"/></svg>Then onto Eton (Hollins Academy) and a lovely view of the River Thames along with an array of Antique Shops in the quaint streets.</li>
      <li class="itinerary__item"><svg viewBox="0 0 12 12"><circle cx="6" cy="6" r="5" fill="none" stroke="#333" stroke-width="1.2"/><path d="M3.5 6.2l1.8 1.8 3.4-3.6" fill="none" stroke="#333" stroke-width="1.3"/></svg>Bray Village (Heron Holm), renowed for it’s Gourmandine Star Restaurants &amp; pubs.</li>
      <li class="itinerary__item"><svg viewBox="0 0 12 12"><circle cx="6" cy="6" r="5" fill="none" stroke="#333" stroke-width="1.2"/><path d="M3.5 6.2l1.8 1.8 3.4-3.6" fill="none" stroke="#333" stroke-width="1.3"/></svg>Through picturesque Cookham along to Marlow for some shopping in the boutique shops, small listed buildings and beautiful places for refreshments, along with stunning views of the River Thames form Pellow Crossing.</li>
      <li class="itinerary__item itinerary__item--narrow"><svg viewBox="0 0 12 12"><circle cx="6" cy="6" r="5" fill="none" stroke="#333" stroke-width="1.2"/><path d="M3.5 6.2l1.8 1.8 3.4-3.6" fill="none" stroke="#333" stroke-width="1.3"/></svg>This will be our main tour we offer but again this is flexible. This aims to be around 4-5 hours.</li>
    </ul>
  </div>

  <div class="contact">
    <h3 class="contact__heading">Contact us</h3>
    <div class="contact__row"><svg class="contact__icon" viewBox="0 0 16 16"><circle cx="8" cy="8" r="7.2" fill="none" stroke="#fff"/><path d="M8 3.8a2.6 2.6 0 0 0-2.6 2.6C5.4 8.6 8 11.6 8 11.6s2.6-3 2.6-5.2A2.6 2.6 0 0 0 8 3.8z" fill="none" stroke="#fff"/><circle cx="8" cy="6.4" r=".9" fill="#fff"/></svg><span>14-16 Copperleaf Road, Maidenhead,<br>United Kingdom, SL6 0QX</span></div>
    <div class="contact__row"><svg class="contact__icon" viewBox="0 0 16 16"><circle cx="8" cy="8" r="7.2" fill="none" stroke="#fff"/><path d="M5.2 4.6l1.4-.4 1 2-1 .8a5 5 0 0 0 2.4 2.4l.8-1 2 1-.4 1.4c-3 .4-6.6-3.2-6.2-6.2z" fill="#fff"/></svg><span>+44 1632 960472</span></div>
    <div class="contact__row"><svg class="contact__icon" viewBox="0 0 16 16"><circle cx="8" cy="8" r="7.2" fill="none" stroke="#fff"/><rect x="4" y="5.3" width="8" height="5.6" fill="none" stroke="#fff"/><path d="M4 5.5l4 3 4-3" fill="none" stroke="#fff"/></svg><span>sales@velvetharbour-example.co.uk</span></div>
    <div class="contact__row"><svg class="contact__icon" viewBox="0 0 16 16"><circle cx="8" cy="8" r="7.2" fill="none" stroke="#fff"/><circle cx="8" cy="8" r="4.2" fill="none" stroke="#fff"/><path d="M3.8 8h8.4M8 3.8c-2 2.4-2 6 0 8.4M8 3.8c2 2.4 2 6 0 8.4" fill="none" stroke="#fff" stroke-width=".8"/></svg><span>www.velvetharbour-example.co.uk</span></div>
  </div>

  <div class="castle-photo" role="img" aria-label="Photo of Ashdene Keep viewed from the long walk with visitors on the path"></div>
</section>

<section class="leaflet leaflet--back">
  <div class="guards-photo" role="img" aria-label="Photo of Ormsby Crown House forecourt during the Parade of the Lancers in red tunics"></div>
  <div class="palace-photo" role="img" aria-label="Photo of Ormsby Crown House and its memorial with red and yellow tulip beds in front"></div>

  <div class="tour-copy">
    <p><span class="tour-copy__heading">We offer London based tours including:</span><br>Farrowdale Hall Palace, Oxford and Durnford Palace, Greyrock Ring and Bath, The Cotswolds, Stratford and Pendry Castle, Lorrimer Outlet Village.</p>
    <p>Also bespoke Tours can be arranged. We can personalise any tour to your requirements.</p>
    <p>Experienced friendly Chauffeur’s, no request too big or small.</p>
  </div>

  <div class="location-map" role="img" aria-label="Street map of Maidenhead with the office location marked"></div>

  <div class="contact">
    <h3 class="contact__heading">Contact us</h3>
    <div class="contact__row"><svg class="contact__icon" viewBox="0 0 16 16"><circle cx="8" cy="8" r="7.2" fill="none" stroke="#fff"/><path d="M8 3.8a2.6 2.6 0 0 0-2.6 2.6C5.4 8.6 8 11.6 8 11.6s2.6-3 2.6-5.2A2.6 2.6 0 0 0 8 3.8z" fill="none" stroke="#fff"/><circle cx="8" cy="6.4" r=".9" fill="#fff"/></svg><span>14-16 Copperleaf Road, Maidenhead,<br>United Kingdom, SL6 0QX</span></div>
    <div class="contact__row"><svg class="contact__icon" viewBox="0 0 16 16"><circle cx="8" cy="8" r="7.2" fill="none" stroke="#fff"/><path d="M5.2 4.6l1.4-.4 1 2-1 .8a5 5 0 0 0 2.4 2.4l.8-1 2 1-.4 1.4c-3 .4-6.6-3.2-6.2-6.2z" fill="#fff"/></svg><span>+44 1632 960472</span></div>
    <div class="contact__row"><svg class="contact__icon" viewBox="0 0 16 16"><circle cx="8" cy="8" r="7.2" fill="none" stroke="#fff"/><rect x="4" y="5.3" width="8" height="5.6" fill="none" stroke="#fff"/><path d="M4 5.5l4 3 4-3" fill="none" stroke="#fff"/></svg><span>sales@velvetharbour-example.co.uk</span></div>
    <div class="contact__row"><svg class="contact__icon" viewBox="0 0 16 16"><circle cx="8" cy="8" r="7.2" fill="none" stroke="#fff"/><circle cx="8" cy="8" r="4.2" fill="none" stroke="#fff"/><path d="M3.8 8h8.4M8 3.8c-2 2.4-2 6 0 8.4M8 3.8c2 2.4 2 6 0 8.4" fill="none" stroke="#fff" stroke-width=".8"/></svg><span>www.velvetharbour-example.co.uk</span></div>
  </div>
</section>

</body>
</html>
```